Website redesign for a Cloud Advisory business

We are looking to revisit our existing brand and website, with a view to updating both. Looking for concepts and designs for how the website might look, flow and feel. Current website is: www.brellomint.com.au

Scope and Deliverables: Concept design for the home page and one internal page.

We do not expect you to design all the pages and all the elements of the website at this stage.

This job is not for the full website design, but just for concepts that we can start with when we go into the full website design.

We would love to see a design feature based on our name, logo, or industry, which can run through banners and other collateral (twitter banner, ads on Google, corporate documents etc).

We want the brand to properly depict what we bring/deliver to businesses when consulting to them and this should extend to the colour scheme, logo, font (perhaps updated) and copy (which will be supplied).

Our brand should suitably communicate our ability, knowledge and extensive experience within the Cloud space.

It should express and evoke credibility, knowledge and understanding of the Cloud space, independence, gravitas, reliability, efficiency, trust, expertise, approachability, service delivery but be uncomplicated, practical and use plain speaking language.

Colours that reinforce this might include: Blues, blacks, silver, white, grey and our existing orange.

Website designs that we like or have referenced include:

Varnolift: http://varnolift.com.au/ - This has good information but looks a little amateur in it’s cartoon like design and colour scheme. Also, this seems to be aimed at clients more interested in price than design and what we are going for is a little more high end.

Pendramoor: https://www.pendramoor.com.au/ - This site has merit in its’ setup but little call to action on the home page, especially before the scroll line. I like the set up of the Case Studies page however I’d look to make it more prominent by having it set up 3 across rather than the 4 they have. Something such as this: https://www.qandelby.com/case-studies

Tolvane: http://www.tolvane.com.au/#home4 - This page is a good one as far as selling services and information on the company. I quite like it.

MirefoldIT: http://www.mirefoldit.com.au/ - While I don’t think is particularly creative, it does practically depict the services we offer in a fairly clear way and might be a bit of a basic (albeit dull) template to follow.

JDP: https://store.jdp.com/us/Product-Family/JDP-Advisory-Services/JDP-Cloud-Advisory-Service/p/JDP-Services-Cloud-Advisory - This offers substantial information but is probably a little confusing although the roll-over drop down menus have merit.

ZEV: http://www.zev.net.au/en/services/ - While this in not quite what we are looking for, the colour scheme gives it more gravitas and quality.

As another reference, this website and the way they present their case studies is also something we like, although I’d like them shown 3 up, side by side…. https://www.qandelby.com/case-studies.

We have added a page layout and page purpose document.

Target Market(s)

Corporates, small - medium business, direct referrals, via search results

Industry/Entity Type

Business

Number of Pages Required

1 page

Font styles to use
Sans Serif

Colors
85abd2
0455a3
000000
f37122
5c5c5c

Requirements
Must have
• Website must be mobile device compatible.
• Concept design for the home page.
Nice to have
• We would love to see a design feature based on our name, logo, or industry, which can run through banners and other collateral (twitter banner, ads on Google, corporate documents etc).

```html
<!DOCTYPE html>
<html lang="en">
<head>
<meta charset="utf-8">
<title>Brellomint – Cloud Advisory</title>
<link href="https://fonts.googleapis.com/css2?family=Open+Sans:wght@400;600;700&family=Montserrat:wght@400;500;600&display=swap" rel="stylesheet">
<style>
:root{
  --orange:#f37122;
  --blue:#0455a3;
  --sky:#85abd2;
  --ink:#000000;
  --navy:#0a1f38;
  --footer:#1b1f24;
  --grey:#5c5c5c;
  --light:#f0f2f5;
  --line:#f6c7a8;
  --white:#ffffff;
  --pale-blue:#eef4fa;
}
*{margin:0;padding:0;box-sizing:border-box}
html,body{width:1200px;height:3025px;overflow:hidden}
body{font-family:"Open Sans",Arial,sans-serif;color:var(--grey);background:var(--white);position:relative}
.abs{position:absolute}
.head-font{font-family:"Montserrat","Open Sans",Arial,sans-serif}

/* top bar */
.topbar{left:0;top:0;width:1200px;height:48px;background:var(--ink);color:var(--white);font-size:12px;font-weight:600}
.topbar .welcome{left:70px;top:16px}
.topbar .contact{right:72px;top:14px;display:flex;gap:18px;align-items:center}
.topbar .contact span{display:flex;align-items:center;gap:5px}

/* header */
.header{left:0;top:48px;width:1200px;height:66px;background:var(--white)}
.brand{left:68px;top:16px;display:flex;align-items:center;gap:10px}
.brand-name{font-weight:700;font-size:28px;color:var(--ink);letter-spacing:1px}
.brand-mark{width:20px;height:20px;background:var(--orange)}
.nav{left:460px;top:10px;display:flex;font-size:12px;font-weight:600;color:var(--ink)}
.nav a{display:block;padding:11px 14px;color:var(--ink);border:2px solid transparent;margin-right:10px}
.nav a.active{border-color:var(--orange)}

/* hero */
.hero{left:0;top:114px;width:1200px;height:591px;background:linear-gradient(120deg,#0d2036 0%,#16355c 38%,#0b1c31 68%,#1f2d3e 100%)}
.hero-title{left:0;top:296px;width:1200px;text-align:center;font-size:44px;font-weight:500;color:var(--white);letter-spacing:1px}
.hero-title em{font-style:normal;color:var(--orange)}
.hero-sub{left:0;top:364px;width:1200px;text-align:center;font-size:22px;font-weight:600;color:var(--white)}
.btn{display:flex;align-items:center;justify-content:center;font-weight:700;color:var(--white);background:var(--orange);font-size:15px}
.btn-read{left:450px;top:443px;width:150px;height:49px;font-size:16px}
.btn-join{left:613px;top:443px;width:150px;height:49px;background:transparent;border:2px solid var(--orange);font-size:16px}

/* booking */
.booking{left:70px;top:631px;width:1062px;height:131px;background:var(--orange)}
.booking h2{position:absolute;left:0;top:15px;width:100%;text-align:center;color:var(--white);font-weight:600;font-size:24px}
.field{position:absolute;top:62px;width:197px;height:38px;background:var(--white);display:flex;align-items:center;gap:7px;padding-left:8px;font-size:12px;color:#888}
.send{position:absolute;left:896px;top:62px;width:92px;height:38px;background:var(--ink);color:var(--white);font-size:13px;font-weight:700;display:flex;align-items:center;justify-content:center;letter-spacing:1px}

/* section headings */
.sec-title{left:0;width:1200px;text-align:center;font-size:44px;font-weight:400;color:var(--ink)}
.rule{height:3px;background:var(--orange);width:76px}

.about-text{left:92px;top:918px;width:1016px;text-align:center;font-size:13px;line-height:22px;color:#888}
.btn-account{left:520px;top:1028px;width:152px;height:49px;font-size:13px;font-weight:600}

/* services */
.card{top:1254px;width:195px;height:362px;border:1px solid var(--line);background:var(--white);text-align:center}
.card.featured{background:var(--pale-blue);border:2px solid var(--orange)}
.card .icon{position:absolute;left:44px;top:30px;width:106px;height:91px;border:1px solid var(--orange);display:flex;align-items:center;justify-content:center}
.card h3{position:absolute;left:0;top:150px;width:100%;font-weight:500;font-size:17px;color:var(--ink)}
.card p{position:absolute;left:18px;top:188px;width:157px;font-size:11px;line-height:16px;color:var(--grey)}
.card .more{position:absolute;left:41px;top:291px;width:112px;height:36px;font-size:13px}

/* team */
.team{left:0;top:1692px;width:1200px;height:506px;background:linear-gradient(180deg,#0e2238 0%,#163050 50%,#0b1a2c 100%)}
.member{top:152px;width:260px;text-align:center;color:var(--white)}
.photo{margin:0 auto;width:150px;height:139px;border:5px solid var(--orange);background:linear-gradient(160deg,#c9d6e4,#6d8299)}
.member h4{margin-top:22px;font-weight:600;font-size:18px}
.member p{margin:8px auto 0;width:196px;font-size:11.5px;font-weight:600;line-height:16px}
.socials{margin-top:14px;display:flex;justify-content:center;gap:12px}
.socials i{display:block;width:28px;height:28px;background:var(--orange)}

/* testimonials & faq */
.col-title{top:2266px;font-size:34px;font-weight:400;color:var(--ink)}
.quote{left:138px;top:2390px;width:415px;height:155px;background:var(--light)}
.quote .mark{position:absolute;left:30px;top:18px;font-size:56px;font-weight:700;color:var(--orange);line-height:1}
.quote p{position:absolute;left:30px;top:68px;width:355px;font-size:12px;line-height:21px;color:#999;text-align:center}
.avatar{left:170px;top:2558px;width:84px;height:84px;border-radius:50%;background:linear-gradient(160deg,#d8e0ea,#7d8ea2)}
.author{left:276px;top:2574px;font-size:13px;color:var(--ink)}
.author small{display:block;font-size:10px;color:#999;margin-top:3px}
.author a{display:block;font-size:10px;color:var(--orange);margin-top:2px}
.dots{left:505px;top:2577px;display:flex;gap:6px}
.dots i{display:block;width:9px;height:9px;border-radius:50%;background:#ccc}
.dots i.on{background:var(--orange)}

.faq-head{left:587px;top:2390px;width:469px;height:48px;background:var(--blue);color:var(--white);font-size:12px;display:flex;align-items:center;padding-left:16px;gap:10px}
.faq-body{left:587px;top:2438px;width:469px;height:142px;border:1px solid #e2e8ef;border-top:none;padding:26px 34px;font-size:12.5px;line-height:22px;color:var(--grey)}
.faq-item{left:587px;width:469px;height:46px;background:var(--light);font-size:12px;color:var(--ink);display:flex;align-items:center;padding-left:14px;gap:10px}
.dot{width:9px;height:9px;border-radius:50%;background:var(--orange)}
.caret{position:absolute;right:18px;top:50%;margin-top:-4px;width:0;height:0;border-top:4px solid transparent;border-bottom:4px solid transparent;border-left:5px solid var(--orange)}
.caret.down{border-left:4px solid transparent;border-right:4px solid transparent;border-top:5px solid var(--white);border-bottom:none;margin-top:-2px}

/* footer */
.footer{left:0;top:2780px;width:1200px;height:210px;background:var(--footer)}
.footer h5{position:absolute;top:18px;font-size:12px;font-weight:700;color:var(--orange)}
.footer .about{position:absolute;left:155px;top:42px;width:255px;font-size:11.5px;line-height:19px;color:#7a8088}
.post{position:absolute;left:452px;display:flex;gap:10px}
.thumb{width:74px;height:36px;background:linear-gradient(90deg,var(--sky),#3a5878)}
.post div{font-size:9.5px;line-height:13px;color:#7a8088}
.post b{display:block;font-weight:400;color:var(--orange);font-size:10.5px}
.touch{position:absolute;left:752px;display:flex;gap:14px;font-size:11.5px;line-height:17px;color:#7a8088}
.touch a{color:var(--orange)}
.copyright{left:0;top:2990px;width:1200px;height:35px;background:#111418;color:#7a8088;font-size:11.5px;display:flex;align-items:center;justify-content:center}
</style>
</head>
<body>

<div class="abs topbar">
  <div class="abs welcome">Welcome Visitor</div>
  <div class="abs contact">
    <span>Call Us
      <svg width="14" height="14" viewBox="0 0 14 14"><circle cx="7" cy="7" r="6.2" fill="none" stroke="#fff" stroke-width="1.2"/><path d="M5 4l1 1.5-.7.8c.4.9 1.1 1.6 2 2l.8-.7L9.6 8.6 9 10c-2.6-.3-4.7-2.4-5-5z" fill="#fff"/></svg>
      Today 1-800-555-0142</span>
    <span>
      <svg width="14" height="14" viewBox="0 0 14 14"><circle cx="7" cy="7" r="6.2" fill="none" stroke="#fff" stroke-width="1.2"/><rect x="4" y="5" width="6" height="4" fill="#fff"/></svg>
      info@brellomint.com</span>
  </div>
</div>

<header class="abs header">
  <div class="abs brand"><span class="brand-name">BRELLOMINT</span><span class="brand-mark"></span></div>
  <nav class="abs nav">
    <a class="active">HOME</a><a>ABOUT</a><a>SERVICES</a><a>PAGES</a><a>BLOG</a><a>CONTACT</a><a>SHOP</a>
  </nav>
</header>

<section class="abs hero" role="img" aria-label="Photo of a consultant working on a laptop at a desk"></section>
<h1 class="abs hero-title head-font">FAST, <em>SECURE</em>, RELIABLE</h1>
<p class="abs hero-sub">Independent cloud advice for growing businesses.</p>
<div class="abs btn btn-read">Read More...</div>
<div class="abs btn btn-join">Join Us</div>

<form class="abs booking">
  <h2 class="head-font">Book a Free Consultation</h2>
  <div class="field" style="left:72px"><svg width="16" height="16" viewBox="0 0 16 16"><circle cx="8" cy="5" r="3.5" fill="#000"/><path d="M1.5 15c0-4 3-6 6.5-6s6.5 2 6.5 6z" fill="#000"/></svg>Your Name</div>
  <div class="field" style="left:275px"><svg width="16" height="12" viewBox="0 0 16 12"><rect x=".7" y=".7" width="14.6" height="10.6" fill="none" stroke="#000" stroke-width="1.3"/><path d="M1 1l7 6 7-6" fill="none" stroke="#000" stroke-width="1.3"/></svg>Your Email</div>
  <div class="field" style="left:478px"><svg width="14" height="14" viewBox="0 0 14 14"><rect x=".7" y="1.7" width="12.6" height="11.6" fill="none" stroke="#000" stroke-width="1.3"/><path d="M.7 5h12.6M4 3.5l1.5 5 4-4" stroke="#000" stroke-width="1.3" fill="none"/></svg>Choose Date</div>
  <div class="field" style="left:681px"><svg width="14" height="14" viewBox="0 0 14 14"><circle cx="7" cy="7" r="6.2" fill="none" stroke="#000" stroke-width="1.3"/><path d="M7 3.5V7l2.5 1.5" stroke="#000" stroke-width="1.3" fill="none"/></svg>Choose Time</div>
  <div class="send">SEND</div>
</form>

<h2 class="abs sec-title head-font" style="top:816px">Who We Are</h2>
<div class="abs rule" style="left:585px;top:876px"></div>
<p class="abs about-text">We are independent cloud advisors who help businesses choose, plan and move to the systems that suit them. With years of hands-on experience across accounting, inventory, point of sale, job management and CRM platforms, we give plain, practical advice with no vendor ties. We work alongside your team from first review to go-live, so your move to the cloud is clear, secure and on budget, and your people are ready to use it from day one.</p>
<div class="abs btn btn-account">Create An Account</div>

<h2 class="abs sec-title head-font" style="top:1138px">Our Services</h2>
<div class="abs rule" style="left:570px;top:1206px"></div>

<svg width="0" height="0" style="position:absolute">
  <defs>
    <g id="server-icon">
      <rect x="0" y="0" width="44" height="10" fill="none" stroke="#f37122" stroke-width="2.2"/>
      <rect x="0" y="15" width="44" height="10" fill="none" stroke="#f37122" stroke-width="2.2"/>
      <rect x="4" y="4" width="20" height="2.5" fill="#f37122"/>
      <rect x="4" y="19" width="20" height="2.5" fill="#f37122"/>
      <circle cx="36" cy="5" r="1.6" fill="#f37122"/><circle cx="36" cy="20" r="1.6" fill="#f37122"/>
      <path d="M22 25v6M8 35h28M8 31v4M36 31v4M22 31v4M8 31h28" stroke="#f37122" stroke-width="2.2" fill="none"/>
    </g>
  </defs>
</svg>

<div class="abs card" style="left:70px">
  <div class="icon"><svg width="44" height="37"><use href="#server-icon"/></svg></div>
  <h3 class="head-font">System Selection</h3>
  <p>Find the right systems for you. Devise a cloud strategy. Inventory Management. Point of Sale. Job Management. Time &amp; Attendance. CRM.</p>
  <div class="btn more">See More...</div>
</div>
<div class="abs card featured" style="left:285px">
  <div class="icon" style="left:43px;top:29px"><svg width="44" height="37"><use href="#server-icon"/></svg></div>
  <h3 class="head-font" style="top:149px">Account Systems</h3>
  <p style="left:17px;top:187px">Find the right systems for you. Devise a cloud strategy. Inventory Management. Point of Sale. Job Management. Time &amp; Attendance. CRM.</p>
  <div class="btn more" style="left:40px;top:290px">See More...</div>
</div>
<div class="abs card" style="left:502px">
  <div class="icon"><svg width="44" height="37"><use href="#server-icon"/></svg></div>
  <h3 class="head-font">Integration</h3>
  <p>Find the right systems for you. Devise a cloud strategy. Inventory Management. Point of Sale. Job Management. Time &amp; Attendance. CRM.</p>
  <div class="btn more">See More...</div>
</div>
<div class="abs card" style="left:718px">
  <div class="icon"><svg width="44" height="37"><use href="#server-icon"/></svg></div>
  <h3 class="head-font">Business Inventory</h3>
  <p>Find the right systems for you. Devise a cloud strategy. Inventory Management. Point of Sale. Job Management. Time &amp; Attendance. CRM.</p>
  <div class="btn more">See More...</div>
</div>
<div class="abs card" style="left:932px">
  <div class="icon"><svg width="44" height="37"><use href="#server-icon"/></svg></div>
  <h3 class="head-font">Job Management</h3>
  <p>Find the right systems for you. Devise a cloud strategy. Inventory Management. Point of Sale. Job Management. Time &amp; Attendance. CRM.</p>
  <div class="btn more">See More...</div>
</div>

<section class="abs team" role="img" aria-label="Dusky city skyline backdrop in deep blue">
  <h2 class="abs sec-title head-font" style="top:26px;color:#fff">Meet The Geeks</h2>
  <div class="abs member" style="left:45px">
    <div class="photo" role="img" aria-label="Portrait of team member"></div>
    <h4 class="head-font">Dorian Keswick</h4>
    <p>Nulla facilisi. Aenean nec eros. Vestibulum ante ipsum primis in faucibu. Suspendisse congue 1986.</p>
    <div class="socials"><i></i><i></i><i></i><i></i></div>
  </div>
  <div class="abs member" style="left:330px">
    <div class="photo" role="img" aria-label="Portrait of team member"></div>
    <h4 class="head-font">Dorian Keswick</h4>
    <p>Nulla facilisi. Aenean nec eros. Vestibulum ante ipsum primis in faucibu. Suspendisse congue 1986.</p>
    <div class="socials"><i></i><i></i><i></i><i></i></div>
  </div>
  <div class="abs member" style="left:615px">
    <div class="photo" role="img" aria-label="Portrait of team member"></div>
    <h4 class="head-font">Dorian Keswick</h4>
    <p>Nulla facilisi. Aenean nec eros. Vestibulum ante ipsum primis in faucibu. Suspendisse congue 1986.</p>
    <div class="socials"><i></i><i></i><i></i><i></i></div>
  </div>
  <div class="abs member" style="left:880px">
    <div class="photo" role="img" aria-label="Portrait of team member"></div>
    <h4 class="head-font">Dorian Keswick</h4>
    <p>Nulla facilisi. Aenean nec eros. Vestibulum ante ipsum primis in faucibu. Suspendisse congue 1986.</p>
    <div class="socials"><i></i><i></i><i></i><i></i></div>
  </div>
</section>

<h2 class="abs col-title head-font" style="left:116px">Testimonails</h2>
<div class="abs rule" style="left:118px;top:2318px"></div>
<div class="abs quote">
  <div class="mark">“</div>
  <p>Their advice made our move to the cloud simple. We chose the right systems first time and our team was up and running within weeks.</p>
</div>
<div class="abs avatar" role="img" aria-label="Client portrait"></div>
<div class="abs author">Marisol Fenwick<small>CEO &amp; Founder Harbourline</small><a>www.brellomint.com</a></div>
<div class="abs dots"><i class="on"></i><i></i><i></i></div>

<h2 class="abs col-title head-font" style="left:590px">Frequently Asked Questions</h2>
<div class="abs rule" style="left:592px;top:2318px"></div>
<div class="abs faq-head"><span class="dot"></span>Rapidiously whiteboard enabled<span class="caret down"></span></div>
<svg class="abs" style="left:605px;top:2437px" width="18" height="10"><path d="M0 0h18L9 9z" fill="#0455a3"/></svg>
<div class="abs faq-body">Efficiently enhance dynamic e-tailers via economically users. Completely empower backend results through tactical Appropriately reintermediate exceptional e-tailers vis-exceptional vortals. Continually implement.</div>
<div class="abs faq-item" style="top:2616px"><span class="dot"></span>Rapidiously whiteboard enabled<span class="caret"></span></div>
<div class="abs faq-item" style="top:2682px"><span class="dot"></span>Rapidiously whiteboard enabled<span class="caret"></span></div>

<footer class="abs footer">
  <h5 style="left:155px">About Us</h5>
  <p class="about">Lorem Ipsum is simply dummy text of the printing and typesetting industry. Lorem Ipsum has been the industry's standard dummy text ever since the 1500s, when an unknown printer took a galley of type and scrambled it to make a type specimen book. It has survived not only five centuries.</p>

  <h5 style="left:452px">From the blog</h5>
  <div class="post" style="top:44px"><span class="thumb" role="img" aria-label="Blog thumbnail"></span><div>December 3,2013<b>Gallery Post</b></div></div>
  <div class="post" style="top:98px"><span class="thumb" role="img" aria-label="Blog thumbnail" style="background:linear-gradient(90deg,#9aa3ad,#4a525c)"></span><div>December 1,2013<b>Useful Resources for designers</b></div></div>
  <div class="post" style="top:152px"><span class="thumb" role="img" aria-label="Blog thumbnail"></span><div>December 1,2013<b>This is an amazing Image Post for<br>everyone</b></div></div>

  <h5 style="left:752px">Get in touch</h5>
  <div class="touch" style="top:44px">
    <svg width="12" height="14" viewBox="0 0 12 14"><path d="M6 0a5 5 0 0 0-5 5c0 4 5 9 5 9s5-5 5-9a5 5 0 0 0-5-5z" fill="#7a8088"/><circle cx="6" cy="5" r="2" fill="#1b1f24"/></svg>
    <span>Harbourline Works Pty<br>118 Wattle Grove Rd, Level 4<br>Carrowmere, NSW 2170</span>
  </div>
  <div class="touch" style="top:112px">
    <svg width="12" height="12" viewBox="0 0 12 12"><path d="M2 1l2 2.5-1 1.3c.8 1.6 2 2.8 3.6 3.6l1.3-1L10.4 9.4 9.5 11C5 10.6 1.4 7 1 2.5z" fill="#7a8088"/></svg>
    <span>+(61) 200 555 0190</span>
  </div>
  <div class="touch" style="top:152px">
    <svg width="12" height="10" viewBox="0 0 12 10"><rect width="12" height="10" fill="#7a8088"/><path d="M0 0l6 5 6-5" fill="none" stroke="#1b1f24"/></svg>
    <a>support@brellomint.com</a>
  </div>
</footer>
<div class="abs copyright">© 2014 Copyright - Brellomint.com. All rights reserved</div>

</body>
</html>
```